Website Design Required

Our client needs a website built from scratch. The website is called Snaps4Easel and is essentially a website that allows you to upload a photo, order and pay and your photo is printed onto a canvas. A closely related website is http://www.framelyhub.co.za/ however this project needs a clean, fresh design that encourages purchases.

Snaps4easel will be a dedicated website which allows users to upload and print a single image for large format printing.

The website flow will consist of the following:

• A landing page will be designed which showcases the product offering and offers simple and easy to understand instructions on how to get a photo up- loaded and delivered to their door.

• An upload page will exist that allows users the ability to upload a photo to the website for printing.

• Once the user has uploaded a photo the website will ensure that the dimensions are good enough for printing onto canvas and advise the user accordingly if it is not suitable.
• Once the photo has passed this validation we will take the user to a new page that will give them a preview of their photo. Here they will be given a chance to place the photo correctly should the need arise.

• Once the user is happy with the photo placement they will click on the next button which will take them to the payment and delivery page whereby they will need to complete all the fields.

• Once done, a final order page will appear confirming all the details of the order as well as payment and delivery information. Once the user is satisfied he can click the order button.

Requirements
Must have
• We will need the following pages designed:
1. Homepage
2. Upload page
3. Photo placement page (which allows users to align their photo onto the canvas)
4. Order & Payment page
Should not have
• The design should not use old style fonts and shoddy illustrations. If illustrations are used they have to be clean, simple, stylish.

```html
<!DOCTYPE html>
<html lang="en">
<head>
<meta charset="utf-8">
<title>Snaps4Easel – Canvas Printing</title>
<link rel="stylesheet" href="https://fonts.googleapis.com/css2?family=Arimo:wght@400;700&family=Questrial&family=Playfair+Display:ital@1&display=swap">
<style>
:root{
  --white:#ffffff;
  --ink:#222222;
  --muted:#8a8a8a;
  --hero-dark:#4e302a;
  --hero-mid:#7d5a52;
  --hero-light:#c39d93;
  --red:#d1505e;
  --green:#7ac75f;
  --blue:#40a0d2;
  --btn-red:#9c2f3a;
  --btn-green:#3f8a33;
  --btn-blue:#1f6e9c;
  --heading:#1f4a6a;
  --deliver:#c9230f;
  --nav-active:#1c1c1c;
  --footer-line:#d9d9d9;
}
*{margin:0;padding:0;box-sizing:border-box}
html,body{width:1200px;height:1025px;overflow:hidden;background:var(--white)}
body{position:relative;font-family:"Arimo",Arial,sans-serif;color:var(--ink)}
.abs{position:absolute}

.topbar{left:0;top:0;width:1200px;height:68px;background:var(--white);z-index:2}
.logo{left:111px;top:0;width:102px;height:143px;background:#111;z-index:3;display:flex;align-items:center;justify-content:center}
.logo span{color:var(--white);font-family:"Questrial",sans-serif;font-size:17px;transform:rotate(-90deg);white-space:nowrap}
.nav{top:20px;height:28px;font-size:15px;font-weight:400;color:#111;line-height:28px}
.nav.active{background:var(--nav-active);color:var(--white);border-radius:3px;text-align:center;width:91px;left:583px}

.hero{left:0;top:68px;width:1200px;height:450px;background:linear-gradient(90deg,var(--hero-dark) 0%,var(--hero-mid) 45%,var(--hero-light) 100%)}
.hero-title{left:60px;top:150px;font-family:"Questrial",sans-serif;font-size:37px;color:var(--white)}
.hero-text{left:60px;top:216px;width:440px;font-size:15.5px;font-weight:700;line-height:21px;color:var(--white)}
.step-art{width:76px;height:70px;border-radius:6px}
.step-arrow{top:366px}
.step-num{width:46px;height:46px;border-radius:50%;background:#111;color:var(--white);font-weight:700;font-size:20px;text-align:center;line-height:46px;box-shadow:0 2px 4px rgba(0,0,0,.5)}

.slider{left:533px;top:111px;width:611px;height:331px;background:var(--white);box-shadow:0 3px 10px rgba(0,0,0,.4)}
.shot{border:3px solid var(--white)}
.slide-btn{top:235px;width:44px;height:44px;border-radius:50%}
.reflection{left:533px;top:446px;width:611px;height:60px;background:linear-gradient(rgba(255,255,255,.18),rgba(255,255,255,0))}

.feature{top:529px;width:356px;height:188px;color:var(--white)}
.feature h2{position:absolute;left:28px;top:12px;font-family:"Questrial",sans-serif;font-weight:400;font-size:28px}
.feature hr{position:absolute;left:22px;top:54px;width:310px;border:0;border-top:2px dotted rgba(255,255,255,.8)}
.feature p{position:absolute;left:22px;top:64px;width:312px;font-size:13.5px;line-height:18.5px}
.feature .more{position:absolute;left:25px;top:138px;width:127px;height:32px;border-radius:2px;font-size:13px;line-height:32px;padding-left:13px;color:var(--white)}
.upload{left:55px;background:var(--red)}
.upload .more{background:var(--btn-red)}
.discover{left:422px;background:var(--green)}
.discover .more{background:var(--btn-green)}
.order{left:789px;background:var(--blue)}
.order .more{background:var(--btn-blue)}

.welcome-title{left:63px;top:746px;font-family:"Questrial",sans-serif;font-size:29px;color:var(--heading)}
.welcome-text{left:66px;top:790px;width:713px;font-size:13.5px;line-height:20.4px;color:var(--muted);text-align:justify}

.testi-title{left:826px;top:748px;font-family:"Questrial",sans-serif;font-size:23px;color:#1a1a1a}
.testi-nav{left:1094px;top:750px;font-size:18px;color:var(--muted)}
.testi-line{left:826px;top:783px;width:294px;border-top:1px solid #e3e3e3}
.quote{left:830px;top:768px;font-family:"Playfair Display",serif;font-size:80px;color:#e4e4e4;line-height:1}
.testi-text{left:830px;top:797px;width:290px;font-size:13.5px;line-height:20px;color:var(--muted);position:absolute}
.testi-name{left:1028px;top:852px;font-family:"Playfair Display",serif;font-style:italic;font-size:21px;color:#222}
.delivery{left:826px;top:899px;width:309px;height:67px;background:var(--deliver);color:var(--white);box-shadow:0 2px 4px rgba(0,0,0,.35)}
.delivery strong{position:absolute;left:14px;top:8px;font-family:"Arimo",sans-serif;font-weight:400;font-size:26px;line-height:25px}

.footer{left:0;top:980px;width:1200px;height:45px;border-top:1px solid var(--footer-line);background:#fafafa}
.footer p{position:absolute;left:66px;top:16px;font-size:13px;color:var(--muted)}
.social{top:995px;width:24px;height:24px;border-radius:50%}
</style>
</head>
<body>

<header>
  <div class="abs topbar"></div>
  <div class="abs logo"><span>Snaps4Easel</span></div>
  <nav>
    <div class="abs nav active">HOME</div>
    <div class="abs nav" style="left:697px">UPLOAD PHOTO</div>
    <div class="abs nav" style="left:858px">PRICING</div>
    <div class="abs nav" style="left:975px">CONTAT US</div>
    <div class="abs nav" style="left:1100px">LOGIN</div>
  </nav>
</header>

<section class="abs hero">
</section>
<h1 class="abs hero-title">Lorem ipsum dolor sit amet</h1>
<p class="abs hero-text">Lorem ipsum dolor sit amet, consectetuer adipiscing elit. Aenean commodo ligula eget dolor. Aenean massa. Cum sociis&nbsp; Lorem ipsum dolor sit amet, consectetuer adipi-scing elit. Aenean commodo ligula</p>

<div class="abs step-art" role="img" aria-label="Camera with photo" style="left:72px;top:349px;background:linear-gradient(#cfe3f2,#8a9aa6)"></div>
<div class="abs step-art" role="img" aria-label="Stack of printed photos" style="left:225px;top:343px;background:linear-gradient(#6fb5e8,#e8a24a)"></div>
<div class="abs step-art" role="img" aria-label="Shopping basket" style="left:367px;top:349px;background:linear-gradient(#ffe04a,#e0a010)"></div>
<svg class="abs step-arrow" style="left:179px" width="32" height="26" viewBox="0 0 32 26"><path d="M0 8h16V0l16 13-16 13v-8H0z" fill="#111"/></svg>
<svg class="abs step-arrow" style="left:320px" width="32" height="26" viewBox="0 0 32 26"><path d="M0 8h16V0l16 13-16 13v-8H0z" fill="#111"/></svg>
<div class="abs step-num" style="left:99px;top:431px">1</div>
<div class="abs step-num" style="left:242px;top:431px">2</div>
<div class="abs step-num" style="left:383px;top:431px">3</div>

<div class="abs slider">
  <div class="abs shot" role="img" aria-label="Canvas print of a swan on dark blue water" style="left:8px;top:8px;width:598px;height:317px;background:linear-gradient(135deg,#0b2b55,#1f5a9a 60%,#0a2448)"></div>
  <div class="abs shot" role="img" aria-label="Second canvas print of a swan" style="left:200px;top:108px;width:410px;height:222px;background:linear-gradient(135deg,#123c70,#2a6cb0 60%,#0c2a52)"></div>
  <div class="abs shot" role="img" aria-label="Third canvas print of a swan" style="left:392px;top:212px;width:218px;height:118px;background:linear-gradient(135deg,#0f3564,#2c70b4 60%,#0a264a)"></div>
</div>
<div class="abs reflection"></div>
<svg class="abs slide-btn" style="left:511px" viewBox="0 0 44 44"><circle cx="22" cy="22" r="22" fill="#6b5550" opacity=".8"/><path d="M25 13l-9 9 9 9" stroke="#3a2a26" stroke-width="4" fill="none"/></svg>
<svg class="abs slide-btn" style="left:1124px" viewBox="0 0 44 44"><circle cx="22" cy="22" r="22" fill="#2a2a2a"/><path d="M19 13l9 9-9 9" stroke="#fff" stroke-width="4" fill="none"/></svg>

<section>
  <article class="abs feature upload">
    <h2>Upload</h2><hr>
    <p>Lorem ipsum dolor sit amet, consectetuer adipiscing elit. Aenean commodo ligula eget dolor. Aenean massa. Cum sociis</p>
    <div class="more">READ MORE <svg width="12" height="14" viewBox="0 0 12 14" style="vertical-align:-2px;margin-left:8px"><path d="M2 1l7 6-7 6" stroke="#fff" stroke-width="3" fill="none"/></svg></div>
  </article>
  <article class="abs feature discover">
    <h2>Discover</h2><hr>
    <p>Lorem ipsum dolor sit amet, consectetuer adipiscing elit. Aenean commodo ligula eget dolor. Aenean massa. Cum sociis</p>
    <div class="more">READ MORE <svg width="12" height="14" viewBox="0 0 12 14" style="vertical-align:-2px;margin-left:8px"><path d="M2 1l7 6-7 6" stroke="#fff" stroke-width="3" fill="none"/></svg></div>
  </article>
  <article class="abs feature order">
    <h2>Order</h2><hr>
    <p>Lorem ipsum dolor sit amet, consectetuer adipiscing elit. Aenean commodo ligula eget dolor. Aenean massa. Cum sociis</p>
    <div class="more">READ MORE <svg width="12" height="14" viewBox="0 0 12 14" style="vertical-align:-2px;margin-left:8px"><path d="M2 1l7 6-7 6" stroke="#fff" stroke-width="3" fill="none"/></svg></div>
  </article>
</section>

<h2 class="abs welcome-title">Welcome to Snaps 4 Easel</h2>
<p class="abs welcome-text">Lorem ipsum dolor sit amet, consectetuer adipiscing elit. Aenean commodo ligula eget dolor. Aenean massa. Cum sociis natoque penatibus et magnis dis parturient montes, nascetur ridiculus mus. Donec qes nec, pellentesque eu, pretium quis, sem. Nulla consequat massa quis enim. Donec pede justo, fringilla vel, aliqu, vulputaLorem ipsum doloLorem ipsum dolor sit amet, consectetuer adipiscing elit. Aenean commodo ligula eget dolor. Aenean massa. Cum sociis natoque penatibus et magnis dis parturient montes, nascetur ridiculus mus. Donec qes nec, pellentesque eu, pretium quis, sem. Nulla consequat massa quis enim. Donec pede justo, fringilla vel, aliqu, vulputaLorem ipsum dolor sit amet, consectetuer adipiscing elit. Aenean commodo ligula eget dolor.</p>

<aside>
  <h3 class="abs testi-title">Testimonials</h3>
  <div class="abs testi-nav">&lt; &gt;</div>
  <div class="abs testi-line"></div>
  <div class="abs quote">&ldquo;</div>
  <p class="abs testi-text">Lorem ipsum dolor sit amet, consectetuer adipi-scing elit. Aenean commodo ligula eget dolor. Aenean massa. Cum sociis</p>
  <div class="abs testi-name">- Mark Dalton</div>
  <div class="abs delivery">
    <strong>FREE DELIVERY<br>IN SA</strong>
    <div class="abs" role="img" aria-label="Framed landscape canvas" style="left:228px;top:10px;width:66px;height:44px;border:3px solid #fff;background:linear-gradient(#f0c090,#7a5030)"></div>
  </div>
</aside>

<footer class="abs footer">
  <p>Copyright © 2011&nbsp; Snaps4easel.com . All Rights Reserved.&nbsp; Terms &amp; Conditions &nbsp; | &nbsp; Privacy Policy</p>
</footer>
<div class="abs social" style="left:1004px;background:#3b5b9a"></div>
<div class="abs social" style="left:1042px;background:#3fa6d8"></div>
<div class="abs social" style="left:1078px;background:#f08a24"></div>
<div class="abs social" style="left:1114px;background:#c8302a"></div>

</body>
</html>
```